Этикетка для флакона моющего средства
Задание на дизайн
Размер
82 мм × 180 мм
Опишите свою организацию или продукт и целевую аудиторию
Этикетка для серии специальных моющих средств, готовых к применению.
Например пятновыводитель для ковров, удалитель следов скотча и фломастера, очиститель ржавчины.
Наши моющие средства применяют как профессиональные уборщики (клинеры), так и «продвинутые домохозяйки».
Основная идея этикетки — современный минималистичный дизайн, отсутствие лишнего информационного шума, на домашней полке и в руках профессионала должно выглядеть как профессиональное средство, где упор на содержимое, на удобство пользования, а не на кричащую этикетку. Обратите внимание на фото, как будет выглядеть сам флакон, на который необходимо сделать этикетку, флакон белого цвета.
Этикетка содержит 3 блока — 1) название и лицевая часть 2) служебная часть (данные производителя, состав, штрих код и т. д. 3) информационная часть по применению — инструкция, перечень удаляемых загрязнений, подходящие поверхности для удаления
Текстовое содержание этикетки — в прилагаемом файле.
Обратите внимание 1) На лицевой части указывается величина pH продукта, при этом цвет этой надписи (или части оформления фронта этикетки) должен быть зеленой в случае кислотного, красной — щелочного, фиолетовый -нейтрального состава, но этот цвет не должен доминировать. 2) Информационную часть хотелось бы выполнить в виде пиктограмм и/или инфографики, там получится 3 группы информационной: «удаляет», «подходит», «применение» . Желательно чтобы в информационной части текста вообще не было, максимум пояснения к рисункам — пиктограммам.
Примеры пиктограмм и этикеток даны в приложении, но это не образцы для копирования, просто направление для творчества Вашего)
Приложите логотипы или другие материалы
Это флакон для которого необходимо разработать этикетку
Это наш логотип
Минималистичный дизайн
лаконичные пиктограммы
Это полный текст этикетки
приятный минимализм, но в нашем случае эко-тему не эксплуатируем
Это наш флакон
Комментарии и пожелания для дизайнеров
Эко тему не эксплуатируем, это для другой линейки, основной показатель здесь - эффективность.
Чтобы не было большого разноцветия в этикетке - цвета полосок в логотипе можно делать того же цвета, что и задан pH средства - то есть зеленым, фиолетовым или оранжевым.

```html
<!DOCTYPE html>
<html lang="ru">
<head>
<meta charset="utf-8">
<title>Универсал растворитель — этикетка</title>
<link rel="stylesheet" href="https://fonts.googleapis.com/css2?family=Jost:wght@200;500;600;700&display=swap">
<style>
  :root {
    --backdrop: #b1b1b1;
    --label: #ffffff;
    --ph-accent: #8a5eb3;
    --ph-soft: #dccbe8;
    --rule: #b79ad3;
  }
  * { margin: 0; padding: 0; box-sizing: border-box; }
  html, body {
    width: 1200px;
    height: 966px;
    overflow: hidden;
    background: var(--backdrop);
    font-family: "Jost", "Helvetica Neue", Arial, sans-serif;
  }
  .label {
    position: absolute;
    left: 380px;
    top: 232px;
    width: 440px;
    height: 502px;
    background: var(--label);
    overflow: hidden;
  }
  .ph-value {
    position: absolute;
    left: 34px;
    top: -22px;
    font-weight: 200;
    font-size: 470px;
    line-height: 1;
    letter-spacing: -18px;
    color: var(--ph-soft);
  }
  .category {
    position: absolute;
    left: 62px;
    top: 198px;
    font-weight: 600;
    font-size: 16px;
    line-height: 1.1;
    color: var(--ph-accent);
  }
  .product-name {
    position: absolute;
    left: 62px;
    top: 262px;
    font-weight: 700;
    font-size: 27px;
    line-height: 1.1;
    letter-spacing: 0.5px;
    color: var(--ph-accent);
  }
  .rule {
    position: absolute;
    left: 62px;
    width: 322px;
    height: 1.5px;
    background: var(--rule);
  }
  .rule--top { top: 328px; }
  .rule--bottom { top: 404px; }
  .ph-type {
    position: absolute;
    left: 62px;
    top: 340px;
    font-weight: 600;
    font-size: 15px;
    color: var(--ph-accent);
  }
  .ph-mark {
    position: absolute;
    left: 355px;
    top: 340px;
    font-weight: 600;
    font-size: 15px;
    color: var(--ph-accent);
  }
  .brand {
    position: absolute;
    left: 62px;
    top: 432px;
    display: flex;
    align-items: center;
    gap: 7px;
    font-weight: 600;
    font-size: 15px;
    color: var(--ph-accent);
  }
  .brand-dot {
    width: 10px;
    height: 10px;
    border-radius: 50%;
    background: var(--ph-accent);
  }
</style>
</head>
<body>
  <section class="label">
    <div class="ph-value">7.5</div>
    <p class="category">Профессиональная<br>химия</p>
    <h1 class="product-name">УНИВЕРСАЛ<br>РАСТВОРИТЕЛЬ</h1>
    <div class="rule rule--top"></div>
    <span class="ph-type">Нейтральный</span>
    <span class="ph-mark">ph</span>
    <div class="rule rule--bottom"></div>
    <div class="brand"><span class="brand-dot"></span>Клирон</div>
  </section>
</body>
</html>
```